I need podcast cover art that could also be incorporated into a website and social media accounts. I originally planned on calling the podcast "Mendral Access Lab" but need to change it to "Mendral Access Roundtable," and its purpose is to educate and inspire people on how we can deliver more affordable, higher quality health care in the United States. The target audience is anyone working in a healthcare related industry (doctors, nurses, healthcare insurers, policymakers involved in writing healthcare policy, etc...). The program will be well-researched and the tone will be upbeat. I will be interviewing experts in healthcare delivery including innovators who have come up with creative solutions to improving healthcare quality where they work. I want to keep the design very clean, simple, and modern looking. Thank you so much - I am looking forward to seeing your designs!

Target Market(s)

working professionals and students in healthcare-related fields

Industry/Entity Type

Health Care

Font styles to use
Sans Serif

Colors

Designer to choose colors to be used in the design.

Requirements
Must have
• very clean, simple and modern looking

```html
<!DOCTYPE html>
<html lang="en">
<head>
<meta charset="utf-8">
<title>Mendral Access Roundtable — Podcast Cover</title>
<link rel="stylesheet" href="https://fonts.googleapis.com/css2?family=Roboto+Condensed:wght@700&display=swap">
<style>
  :root {
    --paper: #ffffff;
    --teal: #5bd8d5;
    --plum: #463f52;
    --lime: #b8dd23;
    --title-white: #ffffff;
  }
  html, body {
    margin: 0;
    padding: 0;
    width: 1200px;
    height: 1200px;
    overflow: hidden;
    background: var(--paper);
  }
  .cover {
    display: block;
    width: 1200px;
    height: 1200px;
  }
  .ring-outer { fill: var(--teal); }
  .ring-inner { fill: var(--plum); }
  .title {
    font-family: "Roboto Condensed", "Arial Narrow", sans-serif;
    font-weight: 700;
    letter-spacing: -1px;
  }
  .title-light { fill: var(--title-white); }
  .title-accent { fill: var(--lime); }
</style>
</head>
<body>
  <svg class="cover" viewBox="0 0 1200 1200" xmlns="http://www.w3.org/2000/svg" role="img" aria-label="Mendral Access Roundtable podcast cover">
    <circle class="ring-outer" cx="836" cy="600" r="744"/>
    <circle class="ring-inner" cx="840" cy="600" r="308"/>
    <text class="title title-light" x="212" y="514" font-size="116">MENDRAL</text>
    <text class="title title-accent" x="210" y="650" font-size="154">ACCESS</text>
    <text class="title title-light" x="212" y="762" font-size="116">ROUNDTABLE</text>
  </svg>
</body>
</html>
```